Nectarine Point of Sale Cards for Grocery Retail Markets

We are looking to update our Nectarine point of sale card and price card. The cards will need to be 7" x 11" with a .125 bleed - one sided. See attached for the old versions. We would like this to use photos that look like true Washington State Peaches. Here are the bullet points we would like to use: - New Crop!- Tree Ripened- Excellent FlavorNOTE: The price card just needs to have a space where a retailer can write in the sale price of the item. See attachment with the white box.

Target Market(s)

Retail market shoppers

Requirements
Must have
• Pictures of Nectarines Only

```html
<!DOCTYPE html>
<html lang="en">
<head>
<meta charset="utf-8">
<title>Nectarine Price Card</title>
<link href="https://fonts.googleapis.com/css2?family=Open+Sans:wght@600;700;800&family=Caveat:wght@400;500&display=swap" rel="stylesheet">
<style>
  :root {
    --backdrop: #e9ecef;
    --card: #ffffff;
    --pink: #e85a6e;
    --green: #15804f;
    --peach-light: #f4c15e;
    --peach-deep: #e8903f;
    --slate: #3a4656;
    --leaf-light: #cfe3c8;
    --leaf: #8fbf86;
    --blush-soft: #f2b9ae;
    --price-box: #f3f3f3;
    --tape: rgba(220, 220, 220, 0.8);
  }
  * { margin: 0; padding: 0; box-sizing: border-box; }
  html, body {
    width: 1200px; height: 808px; overflow: hidden;
    background: var(--backdrop);
  }
  .price-card {
    position: absolute; left: 30px; top: 78px;
    width: 1140px; height: 651px;
    background: var(--card);
    overflow: hidden;
    font-family: "Open Sans", Arial, sans-serif;
  }
  .hero-photo {
    position: absolute; left: 0; top: 0; width: 637px; height: 385px;
    background: linear-gradient(168deg, var(--peach-deep) 0%, var(--peach-light) 50%, #c99a55 78%, var(--slate) 100%);
    clip-path: polygon(0 0, 100% 0, 98% 22%, 100% 48%, 97% 72%, 99% 96%, 78% 99%, 55% 94%, 30% 100%, 8% 95%, 0 98%);
  }
  .tagline {
    position: absolute; left: 52px; top: 22px;
    font-family: "Caveat", cursive; font-weight: 500;
    font-size: 66px; color: #fff; letter-spacing: 1px;
  }
  .headline {
    position: absolute; left: 32px; top: 392px;
    font-weight: 800; font-size: 92px; line-height: 76px;
    color: var(--pink); text-transform: uppercase;
  }
  .benefits {
    position: absolute; left: 34px; top: 550px;
    font-weight: 600; font-size: 37px; line-height: 40px;
    color: var(--green); list-style: none;
  }
  .branch-illustration {
    position: absolute; left: 760px; top: 112px; width: 300px; height: 539px;
    background: linear-gradient(180deg, var(--leaf-light) 0%, var(--leaf) 35%, var(--blush-soft) 55%, var(--leaf) 75%, var(--leaf-light) 100%);
    border-radius: 150px 150px 40px 40px;
    opacity: 0.55;
  }
  .price-slot {
    position: absolute; left: 410px; top: 405px;
    width: 318px; height: 205px;
    background: var(--price-box);
    transform: rotate(-3deg);
    box-shadow: 0 1px 3px rgba(0,0,0,0.08);
  }
  .price-slot .tape {
    position: absolute; width: 90px; height: 34px; background: var(--tape);
  }
  .price-slot .tape-top { left: -20px; top: -14px; transform: rotate(-35deg); }
  .price-slot .tape-bottom { right: -30px; bottom: -6px; transform: rotate(-35deg); }
  .price-slot .price {
    position: absolute; left: 110px; top: 58px;
    font-family: "Caveat", cursive; font-size: 62px; color: #111;
  }
  .brand {
    position: absolute; left: 738px; top: 24px;
    display: flex; align-items: center; gap: 14px;
  }
  .brand-mark {
    width: 74px; height: 74px; border-radius: 50%; background: var(--pink);
  }
  .brand-name {
    font-weight: 700; font-size: 21px; line-height: 22px; color: var(--green);
  }
  .product-line {
    position: absolute; left: 1083px; top: 28px;
    writing-mode: vertical-rl;
    font-weight: 700; font-size: 31px; letter-spacing: 1px;
    color: var(--green); text-transform: uppercase;
  }
</style>
</head>
<body>
  <main class="price-card">
    <div class="hero-photo" role="img" aria-label="Photo of ripe nectarines on a dark wooden table"></div>
    <p class="tagline">taste the difference</p>

    <h1 class="headline">New<br>Crop!</h1>
    <ul class="benefits">
      <li>Tree Ripened</li>
      <li>Excellent Flavor</li>
    </ul>

    <div class="branch-illustration" role="img" aria-label="Botanical illustration of a nectarine branch with two fruits and leaves"></div>

    <div class="price-slot">
      <span class="tape tape-top"></span>
      <span class="tape tape-bottom"></span>
      <span class="price">$5</span>
    </div>

    <div class="brand">
      <span class="brand-mark"></span>
      <span class="brand-name">Cascade Orchard<br>Growers Council</span>
    </div>

    <p class="product-line">Washington State Nectarines</p>
  </main>
</body>
</html>
```